TRNV LLP website - revamping our website after 23 years

Our website needs a complete overhaul. The purpose of this exercise is to provide us with your vision of what you think the website should look like. We don't need the website to be created or coded. Just need creative designs.

We have a four sites that we would like to base our website on;

We like the simplicity of Fairwicks, the style of Pemberly Strand and Kettridge.

http://www.pemberlystrand-example.com/en/toronto-ontario/
http://www.fairwicks-example.ca/
hallkettridge-example.com
http://www.vendrupe-example.com/our-professionals.html

We have a logo that we would like to use which will be attached below. We need to keep our website looking very professional as we have a large number of high net worth clients.
Updates

Hi, We've received some good website designs but they appear to be the same type of template websites we've received in the past - this is not what we're looking for. What we want is a unique website that is modelled on the following three company websites: http://www.fairwicks-example.ca/ www.hallkettridge-example.com/ http://www.pemberlystrand-example.com/en/toronto-ontario/

Thank you everyone for your designs. I will be posting updates and my comments on the various designs in the next day - I want to thank you for the creative designs I see. I thought i would explain a bit about our firm and perhaps it can help when you design the theme of our website: - Our firm is like a family and our clients are truly like our friends. We have close knit relationships in and outside of the office with staff and clients. - We are an 'out of the box' type of firm. We operate differently than most firms and that's a differentiating factor in what makes us who we are - Our slogan is "Count on us" which is a testament to the way we run our practice - We would like an open, fresh, clean look to our website - we don't want the landing page to be overly long or complex because we have limited time to update the website and limited content That's it for the time being - when things come to mind I will post them here.

Can we try a design as follows: - make the website look very similar to www.fairwicks-example.ca - use the same background colour - Keep the same black top but insert our logo - incorporate some of the content from our current website www.trnv-example.com

I have been away dealing with a personal matter. I will look into these websites tomorrow afternoon and provide more feedback / info on the top designer. Thank you

Hi designers, I want to apologize for the delay. I plan on wrapping things up within the next few days. I will go through a few of the top designs and offer my comments. Thank you for your patience.

Target Market(s)

Mainly our current clients - We have a large number of high net worth individuals as clients.

Industry/Entity Type

Accounting

Number of Pages Required

1 page

Requirements
Must have
• Please model website on the websites indicated above.
• Our current website is www.trnv-example.com. It's dark, cluttered and not inviting. We want a fresh, clean website. Please incorporate the logo's attached below.

```html
<!DOCTYPE html>
<html lang="en">
<head>
<meta charset="utf-8">
<title>TRNV LLP — Chartered Professional Accountants</title>
<link rel="stylesheet" href="https://fonts.googleapis.com/css2?family=Open+Sans:wght@400;600;700&family=Cinzel:wght@400&family=Droid+Serif&display=swap">
<style>
:root{
  --page-bg:#e6e6e6;
  --topbar:#1f2022;
  --header:#45474b;
  --white:#ffffff;
  --ink:#2f2f2f;
  --nav-ink:#333333;
  --accent-blue:#3aaee0;
  --heading-plum:#9c2360;
  --green:#9ed46b;
  --promo-title:#1d5072;
  --footer-ink:#222222;
  --footer-link:#6a6a6a;
  --field:#e6e6e6;
  --field-ink:#6f6f6f;
  --icon:#777777;
}
*{box-sizing:border-box;margin:0;padding:0}
html,body{width:1200px;height:1110px;overflow:hidden;background:var(--page-bg);font-family:"Open Sans",Arial,sans-serif}
.site{position:absolute;left:15px;top:15px;width:1170px;height:1080px;background:var(--white);box-shadow:0 0 4px rgba(0,0,0,.15)}
.tagline-bar{position:absolute;left:0;top:0;width:100%;height:30px;background:var(--topbar);color:#a9a9a9;font-family:"Cinzel",Georgia,serif;font-size:11px;letter-spacing:.4px;text-align:center;line-height:30px}
.masthead{position:absolute;left:0;top:30px;width:100%;height:95px;background:var(--header)}
.brand{position:absolute;left:422px;top:14px;display:flex;align-items:center;gap:18px}
.brand-mark{width:62px;height:62px;border:none;background:#5f6166}
.brand-name{font-family:"Cinzel",Georgia,serif;font-size:46px;color:#f2f2f2;letter-spacing:1px}
.hero{position:absolute;left:0;top:125px;width:100%;height:415px;background:var(--white);overflow:hidden}
.hero-photo{position:absolute;left:0;top:0;width:100%;height:100%;background:linear-gradient(90deg,#ffffff 0%,#ffffff 32%,#eef1f2 52%,#d9dde0 70%,#c9cdd1 85%,#e4e6e8 100%)}
.nav{position:absolute;left:200px;top:30px;display:flex;gap:0;list-style:none}
.nav li{font-size:12.5px;font-weight:600;color:var(--nav-ink);margin-right:47px;position:relative;padding-bottom:6px}
.nav li.current::after{content:"";position:absolute;left:0;right:0;bottom:-3px;height:3px;background:var(--accent-blue)}
.nav li.search{display:flex;align-items:center;gap:6px;margin-right:0}
.intro{position:absolute;left:88px;top:110px;width:560px}
.intro h1{font-size:26px;font-weight:700;color:var(--heading-plum);margin-bottom:18px}
.intro p{font-size:14.2px;line-height:21.6px;font-weight:600;color:var(--ink)}
.promo-band{position:absolute;left:0;top:540px;width:100%;height:160px;background:var(--green)}
.promo{position:absolute;top:25px;display:flex}
.promo-art{width:90px;height:100px;border-radius:4px}
.promo-text{margin-left:8px;padding-top:35px}
.promo-text h2{font-size:18px;font-weight:700;color:var(--promo-title);line-height:20px}
.promo-text p{font-size:12.5px;font-weight:600;color:var(--white);line-height:17.5px}
.footer{position:absolute;left:0;top:700px;width:100%;height:330px}
.footer h3{font-size:16px;font-weight:600;color:var(--footer-ink);margin-bottom:8px}
.footer-links{position:absolute;left:66px;top:34px}
.footer-links ul{list-style:none}
.footer-links li{font-size:16px;color:var(--footer-link);line-height:24.8px}
.quick-contact{position:absolute;left:253px;top:34px;width:250px}
.field{height:30px;background:var(--field);margin-bottom:7px;padding:7px 17px;font-size:14px;color:var(--field-ink)}
.field.message{height:75px}
.send{width:105px;height:40px;background:#0f0f0f;color:#fff;font-weight:600;font-size:14px;text-align:center;line-height:38px;border:1px solid #555;margin-top:6px}
.contact{position:absolute;left:593px;top:34px}
.contact-row{display:flex;gap:12px;font-size:16px;color:var(--footer-link);line-height:21.5px}
.contact-row svg{flex:none;margin-top:3px}
.footer-brand{position:absolute;left:861px;top:85px;width:246px;height:77px;background:var(--header);display:flex;align-items:center;justify-content:center;gap:12px}
.footer-brand .brand-mark{width:30px;height:30px}
.footer-brand .brand-name{font-size:30px}
.legal{position:absolute;left:0;top:1030px;width:100%;height:50px;background:linear-gradient(#e9e9e9,#f7f7f7);font-size:11px;color:#555;text-align:center;line-height:50px;letter-spacing:.2px}
</style>
</head>
<body>
<div class="site">
  <div class="tagline-bar">We bring over 100 years of experience of valuable experience to the practice of public accounting</div>
  <header class="masthead">
    <div class="brand"><div class="brand-mark"></div><span class="brand-name">TRNV LLP</span></div>
  </header>

  <section class="hero">
    <div class="hero-photo" role="img" aria-label="Photo of three accountants reviewing documents together at an office table"></div>
    <ul class="nav">
      <li class="current">HOME</li><li>ABOUT TRNV</li><li>SERVICES</li><li>LIBRARY</li><li>LINKS</li><li>CAREERS</li><li>CONTACT US</li>
      <li class="search">SEARCH <svg width="14" height="14" viewBox="0 0 14 14"><circle cx="5.5" cy="5.5" r="4" fill="none" stroke="#222" stroke-width="1.8"/><line x1="8.5" y1="8.5" x2="13" y2="13" stroke="#222" stroke-width="2.2"/></svg></li>
    </ul>
    <div class="intro">
      <h1>Welcome to TRNV</h1>
      <p>TRNV, Tarrow Renick Neville Vane LLP Chartered Accountants, is a full-service, public accounting firm, primarily serving the small and mid-size, entrepreneurial business and professional sectors in Toronto Canada. TRNV’s experienced partners and professional, support staff strive to provide accounting and advisory services using an invaluable personal approach, designed to meet each client’s individual needs. This “personal touch”, combined with a full range of accounting, auditing, tax compliance and planning services allows TRNV to meet all your business and personal accounting requirements.</p>
    </div>
  </section>

  <section class="promo-band">
    <div class="promo" style="left:110px">
      <div class="promo-art" role="img" aria-label="Illustration of a folded newspaper" style="background:linear-gradient(160deg,#f4f4f0,#c9c9c2)"></div>
      <div class="promo-text"><h2>TRNV NEWS</h2><p>Check out the latest happenings in<br>TRNV and subscribe for our latest<br>updates</p></div>
    </div>
    <div class="promo" style="left:450px">
      <div class="promo-art" role="img" aria-label="Illustration of a desk calculator" style="width:78px;background:linear-gradient(#8a8d90,#4a4d50)"></div>
      <div class="promo-text" style="margin-left:12px"><h2>2015 TAX ESTIMATOR</h2><p>For 2014 Now Online! Please click<br>to begin</p></div>
    </div>
    <div class="promo" style="left:770px">
      <div class="promo-art" role="img" aria-label="Illustration of a blue folder with an arrow" style="background:linear-gradient(135deg,#3b9bd0,#0d4f7a);height:70px;margin-top:15px"></div>
      <div class="promo-text"><h2>TAX TIPS</h2><p>Click here to view Personal Tax<br>Commentary and Tax Guide 2015</p></div>
    </div>
  </section>

  <footer class="footer">
    <div class="footer-links">
      <h3>LINKS</h3>
      <ul><li>ABOUT TRNV</li><li>SERVICES</li><li>LIBRARY</li><li>LINKS</li><li>CAREERS</li><li>CONTACT US</li></ul>
    </div>
    <div class="quick-contact">
      <h3 style="margin-left:3px">QUICK CONTACT</h3>
      <div class="field">Name</div><div class="field">Email</div><div class="field">Phone</div>
      <div class="field message">Message</div>
      <div class="send">SEND</div>
    </div>
    <div class="contact">
      <h3>CONTACT</h3>
      <div class="contact-row"><svg width="14" height="18" viewBox="0 0 14 18"><path d="M7 0a7 7 0 0 0-7 7c0 5 7 11 7 11s7-6 7-11a7 7 0 0 0-7-7z" fill="#777"/><circle cx="7" cy="7" r="2.5" fill="#fff"/></svg>
        <div>The Harlow Centre<br>4720 Elmridge Street<br>Suite 1406<br>Toronto, Ontario<br>Canada, M4R 2J8</div></div>
      <div class="contact-row" style="margin-top:22px;margin-left:-3px"><svg width="18" height="14" viewBox="0 0 18 14"><path d="M1 4c0-3 16-3 16 0v2h-4V4H5v2H1z" fill="#777"/><rect x="3" y="7" width="12" height="7" rx="1" fill="#777"/></svg><div>(416) 555-0140</div></div>
      <div class="contact-row" style="margin-top:22px;margin-left:-3px"><svg width="18" height="16" viewBox="0 0 18 16"><rect x="4" y="0" width="10" height="5" fill="#777"/><rect x="1" y="5" width="16" height="7" rx="1" fill="#777"/><rect x="4" y="10" width="10" height="6" fill="#999"/></svg><div>(416) 555-0199</div></div>
      <div class="contact-row" style="margin-top:22px;margin-left:-3px"><svg width="18" height="13" viewBox="0 0 18 13"><rect x="0.5" y="0.5" width="17" height="12" fill="#777"/><path d="M1 1l8 6 8-6" fill="none" stroke="#fff" stroke-width="1.2"/></svg><div>info@trnv-example.com</div></div>
    </div>
    <div class="footer-brand"><div class="brand-mark"></div><span class="brand-name">TRNV LLP</span></div>
  </footer>

  <div class="legal">COPYRIGHT © 2015 TRNV CHARTERED ACCOUNTANTS.&nbsp; ALL RIGHTS RESERVED.</div>
</div>
</body>
</html>
```